Migration Lawyers

Company: Thornbury & Co Lawyers & Migration Agents

Name: Gavin Rusholt BEc, LLB
Address: Level 19, 71 Pelham Street
Sydney, NSW, Australia 2000

Ph: +61 2 9357 2164
M: 0438261504
E: gavin@permit-nomadra.org.au
W: www.permit-nomadra.org.au

Target Market(s)

Migration Clients

Industry/Entity Type

It Company

Font styles to use
Script

Requirements
Must have
• Logo
Should not have
• Please scale the format to the printing size attached

```html
<!DOCTYPE html>
<html lang="en">
<head>
<meta charset="utf-8">
<title>Thornbury &amp; Co – Business Card</title>
<link rel="stylesheet" href="https://fonts.googleapis.com/css2?family=Tinos:ital,wght@0,400;0,700;1,400;1,700&display=swap">
<style>
  :root {
    --brand-red: #820e17;
    --ink: #111111;
    --paper: #ffffff;
    --backdrop: #1b1b1b;
    --serif: "Tinos", "Times New Roman", serif;
  }
  * { margin: 0; padding: 0; box-sizing: border-box; }
  html, body {
    width: 1200px; height: 731px; overflow: hidden;
    background: var(--backdrop);
    font-family: var(--serif);
  }
  .card {
    position: absolute; left: 107px; top: 94px;
    width: 984px; height: 558px;
    background: var(--paper);
    overflow: hidden;
  }
  .holder {
    position: absolute; right: 30px; top: 28px;
    text-align: right; line-height: 1;
  }
  .holder__name {
    color: var(--brand-red); font-size: 26px; font-weight: 400;
    letter-spacing: 0.2px;
  }
  .holder__degrees {
    margin-top: 5px; color: var(--ink); font-size: 25px; font-style: italic;
  }
  .brand {
    position: absolute; left: 0; right: 0; top: 152px;
    text-align: center; line-height: 1;
  }
  .brand__mark {
    display: block; margin: 0 auto;
    width: 100px; height: 100px; border-radius: 50%;
    background: var(--brand-red);
  }
  .brand__name {
    margin-top: 18px;
    color: var(--brand-red); font-size: 52px; font-weight: 700;
  }
  .brand__tagline {
    margin-top: 6px;
    color: var(--ink); font-size: 22px; font-weight: 700; font-style: italic;
  }
  .contact {
    position: absolute; top: 424px;
    list-style: none; font-size: 24px; color: var(--ink); line-height: 30px;
  }
  .contact--phones { left: 20px; }
  .contact--online { left: 618px; }
  .contact__item { display: flex; align-items: center; gap: 10px; }
  .contact__icon { width: 16px; height: 16px; flex: none; }
  .address-band {
    position: absolute; left: 0; bottom: 0;
    width: 100%; height: 55px;
    background: var(--brand-red); color: var(--paper);
    font-size: 24px; line-height: 55px; text-align: center;
  }
</style>
</head>
<body>
<main class="card">
  <header class="holder">
    <p class="holder__name">GAVIN RUSHOLT</p>
    <p class="holder__degrees">BEc, LLB</p>
  </header>

  <section class="brand">
    <span class="brand__mark" aria-hidden="true"></span>
    <h1 class="brand__name">Thornbury &amp; Co</h1>
    <p class="brand__tagline">Lawyers &amp; Migration Agents</p>
  </section>

  <ul class="contact contact--phones">
    <li class="contact__item">
      <svg class="contact__icon" viewBox="0 0 16 16" aria-hidden="true"><circle cx="8" cy="8" r="6.5" fill="none" stroke="#820e17" stroke-width="1.6"/><path d="M6 4.5c2.5 0 3.5 1.5 3.5 3.5S8.5 11.5 6 11.5" fill="none" stroke="#820e17" stroke-width="1.6"/></svg>
      <span>+612 9357 2164</span>
    </li>
    <li class="contact__item">
      <svg class="contact__icon" viewBox="0 0 16 16" aria-hidden="true"><rect x="4" y="2" width="8" height="13" rx="1" fill="none" stroke="#820e17" stroke-width="1.5"/><rect x="5.5" y="4" width="5" height="3.5" fill="#820e17"/><path d="M5.5 9.5h5M5.5 11.5h5M5.5 13h5" stroke="#820e17" stroke-width="1"/><path d="M10 2V0" stroke="#820e17" stroke-width="1.2"/></svg>
      <span>0438261504</span>
    </li>
  </ul>

  <ul class="contact contact--online">
    <li class="contact__item">
      <svg class="contact__icon" viewBox="0 0 16 16" aria-hidden="true"><rect x="1.5" y="4" width="13" height="9" fill="none" stroke="#820e17" stroke-width="1.5"/><path d="M1.5 4l6.5 5 6.5-5" fill="none" stroke="#820e17" stroke-width="1.5"/></svg>
      <span>gavin@permit-nomadra.org.au</span>
    </li>
    <li class="contact__item">
      <svg class="contact__icon" viewBox="0 0 16 16" aria-hidden="true"><circle cx="7.5" cy="7.5" r="6" fill="none" stroke="#820e17" stroke-width="1.5"/><path d="M1.5 7.5h12M7.5 1.5c-3 3-3 9 0 12M7.5 1.5c3 3 3 9 0 12" fill="none" stroke="#820e17" stroke-width="1.1"/><path d="M9 9l6 2.5-2.5 1-1 2.5z" fill="#820e17"/></svg>
      <span>www.permit-nomadra.org.au</span>
    </li>
  </ul>

  <footer class="address-band">Level 19, 71 Pelham Street, Australia, Sydney, NSW-2000</footer>
</main>
</body>
</html>
```